Business Cards

Business card design for my company.
I would like the card's background colour to be black. You can also see our web site to get an idea of our brand. https://www.dlqmarrowfield.com.au/
- Name
- Email

```html
<!DOCTYPE html>
<html lang="en">
<head>
<meta charset="utf-8">
<title>DLQ Marrowfield – Business Cards</title>
<link rel="stylesheet" href="https://fonts.googleapis.com/css2?family=Montserrat:wght@400;500;700&display=swap">
<style>
  :root {
    --page: #3b3b3b;
    --card: #141414;
    --card-front-a: #1c1c1c;
    --card-front-b: #0c0c0c;
    --green: #1a9a4b;
    --white: #ffffff;
    --muted: #e8e8e8;
  }
  * { margin: 0; padding: 0; box-sizing: border-box; }
  html, body {
    width: 1200px; height: 694px; overflow: hidden;
    background: var(--page);
    font-family: "Montserrat", Arial, sans-serif;
  }
  .canvas {
    position: relative; width: 1200px; height: 694px;
  }
  .card {
    position: absolute; top: 192px;
    width: 540px; height: 310px;
    border-radius: 18px;
    overflow: hidden;
    background: var(--card);
  }
  .card--front { left: 40px; }
  .card--back { left: 620px; }

  .front-texture {
    position: absolute; inset: 0;
    background: linear-gradient(135deg, var(--card-front-a) 0%, var(--card-front-b) 60%, #181818 100%);
  }
  .brand {
    position: absolute;
    display: flex; align-items: center; gap: 12px;
    color: var(--white);
    font-weight: 700;
    white-space: nowrap;
  }
  .brand__dot {
    width: 14px; height: 14px; border-radius: 50%;
    background: var(--green);
  }
  .card--front .brand {
    left: 50%; top: 50%; transform: translate(-50%, -50%);
    font-size: 38px; letter-spacing: 1px;
  }
  .card--back .brand {
    right: 30px; top: 52px;
    font-size: 22px; letter-spacing: 0.5px;
  }
  .card--back .brand__dot { width: 10px; height: 10px; }

  .person {
    position: absolute; left: 30px; top: 96px;
  }
  .person__name {
    color: var(--green); font-weight: 700; font-size: 26px; line-height: 1.1;
  }
  .person__role {
    color: var(--white); font-weight: 400; font-size: 14px; margin-top: 6px;
  }
  .divider {
    position: absolute; left: 30px; right: 30px; top: 170px;
    height: 2px; background: var(--green);
  }
  .contacts {
    position: absolute; left: 30px; top: 190px;
    list-style: none;
  }
  .contacts__item, .location {
    display: flex; align-items: center; gap: 10px;
    color: var(--muted); font-size: 13px; font-weight: 400;
    height: 24px; margin-bottom: 6px;
  }
  .location {
    position: absolute; right: 30px; top: 190px;
  }
  .icon {
    width: 18px; height: 18px; flex: none;
  }
</style>
</head>
<body>
<main class="canvas">

  <section class="card card--front">
    <div class="front-texture" role="img" aria-label="Subtle embossed chevron texture across the black card"></div>
    <div class="brand"><span class="brand__dot"></span>DLQ Marrowfield</div>
  </section>

  <section class="card card--back">
    <div class="brand"><span class="brand__dot"></span>DLQ Marrowfield</div>

    <div class="person">
      <p class="person__name">Neil Hartcombe</p>
      <p class="person__role">General Manager</p>
    </div>

    <div class="divider"></div>

    <ul class="contacts">
      <li class="contacts__item">
        <svg class="icon" viewBox="0 0 18 18" aria-hidden="true">
          <circle cx="9" cy="9" r="9" fill="var(--green)"/>
          <path d="M6 5.2l1.6-.4.9 2-1 .8a5 5 0 0 0 2.9 2.9l.8-1 2 .9-.4 1.6c-3.6.3-7.1-3.2-6.8-6.8z" fill="#fff"/>
        </svg>
        0400 555 218
      </li>
      <li class="contacts__item">
        <svg class="icon" viewBox="0 0 18 18" aria-hidden="true">
          <circle cx="9" cy="9" r="9" fill="var(--green)"/>
          <rect x="4.5" y="6" width="9" height="6.5" rx="0.8" fill="#fff"/>
          <path d="M4.8 6.3L9 9.6l4.2-3.3" fill="none" stroke="var(--green)" stroke-width="1"/>
        </svg>
        info@dlqmarrowfield.com.au
      </li>
      <li class="contacts__item">
        <svg class="icon" viewBox="0 0 18 18" aria-hidden="true">
          <circle cx="9" cy="9" r="9" fill="var(--green)"/>
          <circle cx="9" cy="9" r="4.5" fill="none" stroke="#fff" stroke-width="1.2"/>
          <path d="M4.5 9h9M9 4.5c-2 2.5-2 6.5 0 9M9 4.5c2 2.5 2 6.5 0 9" fill="none" stroke="#fff" stroke-width="1"/>
        </svg>
        www.dlqmarrowfield.com.au
      </li>
    </ul>

    <p class="location">
      <svg class="icon" viewBox="0 0 18 18" aria-hidden="true">
        <circle cx="9" cy="9" r="9" fill="var(--green)"/>
        <path d="M9 4a3.2 3.2 0 0 0-3.2 3.2C5.8 9.6 9 13.5 9 13.5s3.2-3.9 3.2-6.3A3.2 3.2 0 0 0 9 4z" fill="#fff"/>
        <circle cx="9" cy="7.2" r="1.2" fill="var(--green)"/>
      </svg>
      Kelsbury, Tasmania, Australia
    </p>
  </section>

</main>
</body>
</html>
```